Hi Marlene,

I need your help to design another poster for Corporate & Private Catering.

Price List is as follow :

PACK 1: $15 per person (Min 10 people) This includes:
- 10 x Noodle Salads / Pho (All options included)
- 10 x Fresh Ricepaper Rolls
- 10 x Spring Rolls

PACK 1: $20 per person (Min 10 people) This includes:
- 10 x Rice (All options included)
- 10 x Spring Rolls

SPRING ROLLS (Seafood / Vegetarian)
20 Rolls = $30
30 Rolls = $45
40 Rolls = $60
50 Rolls = $75

FRESH RICEPAPER ROLLS
20 Rolls = $50
30 Rolls = $75
40 Rolls = $100
50 Rolls = $125

FRIED RICE (All options included)
- $50 per tray. Serve 5-7 people.

```html
<!DOCTYPE html>
<html lang="en">
<head>
<meta charset="utf-8">
<title>Corporate &amp; Private Catering Price List</title>
<link href="https://fonts.googleapis.com/css2?family=Bree+Serif&family=Andika&family=Baloo+2:wght@600&display=swap" rel="stylesheet">
<style>
  :root {
    --page-bg: #e9e7e4;
    --board: #161616;
    --board-light: #2a2a2a;
    --line: #9a9a9a;
    --text: #f2f2f2;
    --orange: #f6a21b;
    --green: #7ed321;
    --icon: #e9b21c;
    --photo-bowl: #8a5a3a;
    --photo-sauce: #7a1f22;
    --photo-roll: #c9b46a;
    --photo-fresh: #c7c9b8;
    --photo-rice: #c9a24a;
    --photo-pho: #5a3520;
  }
  * { margin: 0; padding: 0; box-sizing: border-box; }
  html, body { width: 1200px; height: 1200px; overflow: hidden; background: var(--page-bg); }
  .poster {
    position: absolute; left: 190px; top: 20px;
    width: 859px; height: 1215px;
    transform: scale(0.955); transform-origin: top left;
    background: radial-gradient(ellipse at 45% 40%, var(--board-light), var(--board) 75%);
    overflow: hidden; color: var(--text);
    font-family: "Andika", sans-serif;
  }
  .frame { position: absolute; left: 17px; top: 17px; right: 17px; bottom: 17px; border: 1px solid var(--line); }
  .abs { position: absolute; }
  .dashed-box { position: absolute; border: 1px dashed var(--line); border-radius: 30px; }
  .dotted-rule { position: absolute; border-top: 2px dotted #777; height: 0; }
  .price-big { position: absolute; font-family: "Baloo 2", sans-serif; font-weight: 600; font-size: 76px; line-height: 1; }
  .orange { color: var(--orange); }
  .green { color: var(--green); }
  .pack-title { position: absolute; font-family: "Bree Serif", serif; font-size: 23px; line-height: 30px; }
  .pack-item { position: absolute; font-size: 19px; line-height: 23px; padding-left: 29px; }
  .pack-item svg { position: absolute; left: 0; top: 2px; width: 20px; height: 20px; }
  .section-title { position: absolute; font-family: "Bree Serif", serif; font-size: 24px; }
  .roll-price { position: absolute; font-size: 26px; line-height: 40px; padding-left: 56px; white-space: nowrap; }
  .roll-price svg { position: absolute; left: 0; top: 0; width: 46px; height: 44px; }
  .roll-price b { font-family: "Baloo 2", sans-serif; font-weight: 600; font-size: 28px; }
  .photo { position: absolute; }
  .photo.round { border-radius: 50%; border: 6px solid #fff; }
  .rice-title { position: absolute; font-family: "Bree Serif", serif; font-size: 24px; text-align: right; line-height: 31px; }
  .rice-note { position: absolute; font-size: 20px; }
</style>
</head>
<body>
<svg width="0" height="0" style="position:absolute">
  <defs>
    <symbol id="dish-icon" viewBox="0 0 20 20">
      <circle cx="10" cy="10" r="9" fill="var(--icon)"/>
      <path d="M7 5v10M13 5v10" stroke="#161616" stroke-width="2" stroke-linecap="round"/>
    </symbol>
    <symbol id="roll-icon" viewBox="0 0 46 44">
      <circle cx="20" cy="22" r="18" fill="none" stroke="var(--icon)" stroke-width="3"/>
      <circle cx="20" cy="22" r="12" fill="none" stroke="var(--icon)" stroke-width="2.5"/>
      <path d="M16 15v14M24 15v14" stroke="var(--icon)" stroke-width="2.5"/>
      <path d="M38 6l6 36M42 6l3 34" stroke="var(--icon)" stroke-width="2"/>
    </symbol>
  </defs>
</svg>

<main class="poster">
  <div class="frame"></div>

  <!-- Photos -->
  <div class="photo round" role="img" aria-label="Bowl of beef noodle salad with herbs" style="left:680px;top:37px;width:200px;height:200px;background:radial-gradient(circle,var(--photo-bowl),#d8c9a8 80%)"></div>
  <div class="photo round" role="img" aria-label="Small bowl of chilli sauce" style="left:662px;top:262px;width:64px;height:64px;border-width:5px;background:var(--photo-sauce)"></div>
  <div class="photo round" role="img" aria-label="Small bowl of soy sauce" style="left:738px;top:258px;width:64px;height:64px;border-width:5px;background:#0e0e0e"></div>
  <div class="photo" role="img" aria-label="Ceramic spoon" style="left:683px;top:333px;width:78px;height:26px;border-radius:14px;background:linear-gradient(90deg,#c9a89a,#f3ece7)"></div>
  <div class="photo" role="img" aria-label="Sliced spring roll with lemon" style="left:607px;top:432px;width:175px;height:185px;border-radius:40% 40% 30% 30%;background:radial-gradient(circle at 50% 60%,#6a8a3a,var(--photo-roll) 55%,transparent 72%)"></div>
  <div class="photo" role="img" aria-label="Fresh ricepaper rolls with basil and dipping sauce" style="left:48px;top:690px;width:165px;height:265px;border-radius:14px;background:linear-gradient(160deg,var(--photo-fresh),#d88a5a 60%,#6c9a4a)"></div>
  <div class="photo round" role="img" aria-label="Plate of fried rice with vegetables" style="left:44px;top:978px;width:180px;height:180px;background:radial-gradient(circle,var(--photo-rice),#e9d8a8 75%)"></div>
  <div class="photo round" role="img" aria-label="Bowl of beef pho with herbs" style="left:724px;top:1072px;width:160px;height:160px;background:radial-gradient(circle,var(--photo-pho),#3a2215 70%)"></div>

  <!-- Pack 1 -->
  <div class="dashed-box" style="left:35px;top:45px;width:304px;height:370px"></div>
  <div class="price-big orange" style="left:54px;top:66px">$15</div>
  <div class="pack-title" style="left:57px;top:147px">per person (Min 10<br>people) This includes:</div>
  <div class="pack-item" style="left:53px;top:229px"><svg><use href="#dish-icon"/></svg>10 x Noodle Salads/Pho<br>(All options included)</div>
  <div class="pack-item" style="left:53px;top:302px"><svg><use href="#dish-icon"/></svg>10 x Fresh Ricepaper Rolls</div>
  <div class="pack-item" style="left:53px;top:353px"><svg><use href="#dish-icon"/></svg>10 x Spring Rolls</div>

  <!-- Pack 2 -->
  <div class="price-big green" style="left:368px;top:62px">$20</div>
  <div class="pack-title" style="left:371px;top:137px">per person (Min 10<br>people) This includes:</div>
  <div class="pack-item" style="left:371px;top:220px"><svg><use href="#dish-icon"/></svg>10 x Rice<br>(All options included)</div>
  <div class="pack-item" style="left:371px;top:293px"><svg><use href="#dish-icon"/></svg>10 x Fresh Ricepaper Rolls</div>
  <div class="pack-item" style="left:371px;top:344px"><svg><use href="#dish-icon"/></svg>10 x Spring Rolls</div>
  <div class="dotted-rule" style="left:372px;top:414px;width:357px"></div>

  <!-- Spring rolls -->
  <div class="section-title" style="left:48px;top:448px">SPRING ROLLS (Seafood / Vegetarian)</div>
  <div class="roll-price" style="left:57px;top:514px"><svg><use href="#roll-icon"/></svg>20 Rolls = <b class="orange">$30</b></div>
  <div class="roll-price" style="left:310px;top:516px"><svg><use href="#roll-icon"/></svg>40 Rolls = <b class="orange">$60</b></div>
  <div class="roll-price" style="left:57px;top:583px"><svg><use href="#roll-icon"/></svg>30 Rolls = <b class="green">$45</b></div>
  <div class="roll-price" style="left:310px;top:585px"><svg><use href="#roll-icon"/></svg>50 Rolls = <b class="green">$75</b></div>
  <div class="dotted-rule" style="left:67px;top:662px;width:563px"></div>

  <!-- Fresh ricepaper rolls -->
  <div class="section-title" style="left:441px;top:703px">FRESH RICEPAPER ROLLS</div>
  <div class="roll-price" style="left:267px;top:771px"><svg><use href="#roll-icon"/></svg>20 Rolls = <b class="orange">$50</b></div>
  <div class="roll-price" style="left:520px;top:773px"><svg><use href="#roll-icon"/></svg>40 Rolls = <b class="orange">$100</b></div>
  <div class="roll-price" style="left:267px;top:840px"><svg><use href="#roll-icon"/></svg>30 Rolls = <b class="green">$75</b></div>
  <div class="roll-price" style="left:520px;top:842px"><svg><use href="#roll-icon"/></svg>50 Rolls = <b class="green">$125</b></div>
  <div class="dotted-rule" style="left:234px;top:929px;width:562px"></div>

  <!-- Fried rice -->
  <div class="dashed-box" style="left:61px;top:997px;width:743px;height:170px"></div>
  <div class="price-big orange" style="left:288px;top:1052px">$50</div>
  <div class="rice-title" style="left:440px;top:1039px;width:260px">FRIED RICE<br>(All options included)</div>
  <div class="rice-note" style="left:470px;top:1108px">per tray. Serve 5-7 people.</div>
</main>
</body>
</html>
```